high end contractor

high end contracting company we do all phases of construction kitchen,bathrooms,etc... please look at my website before you design www.harborkeybuild.com

would love some sort of lines or logo or both

Industry/Entity Type

Construction

Contact Information for Business Card

company name: oak & meridian contracting address: 318 fenwick st mount Vernon ny 10552 email: harborkeybuild@mailbrook.com website: www.harborkeybuild.com office#: 914-208-3916 fax#: 914-208-5523 dominic valtersen mobile# 917-526-0389

```html
<!DOCTYPE html>
<html lang="en">
<head>
<meta charset="utf-8">
<title>Oak &amp; Meridian Contracting — Business Card</title>
<link href="https://fonts.googleapis.com/css2?family=Montserrat:wght@700&family=Questrial&display=swap" rel="stylesheet">
<style>
  :root {
    --backdrop: #e4e6e8;
    --card-taupe: #b3aba7;
    --band-dark: #2a2929;
    --teal: #3fc1bf;
    --ink: #2b2828;
    --white: #ffffff;
    --photo-light: #d9d6d4;
    --photo-mid: #a39e9b;
    --photo-dark: #5b5755;
  }
  * { margin: 0; padding: 0; box-sizing: border-box; }
  html, body { width: 1200px; height: 777px; overflow: hidden; }
  body {
    background: var(--backdrop);
    font-family: "Questrial", "Century Gothic", sans-serif;
    display: flex;
    flex-direction: column;
    align-items: center;
    justify-content: center;
    gap: 28px;
  }
  .card {
    position: relative;
    width: 620px;
    height: 354px;
    overflow: hidden;
    box-shadow: 0 6px 18px rgba(0,0,0,.18);
  }

  /* ---------- info side ---------- */
  .card--info { background: var(--card-taupe); color: var(--ink); }
  .holder-name {
    position: absolute; left: 40px; top: 30px;
    font-size: 30px; letter-spacing: 2px; text-transform: uppercase;
  }
  .holder-mobile {
    position: absolute; left: 250px; top: 76px;
    display: flex; align-items: center; gap: 10px; font-size: 18px;
  }
  .badge {
    width: 20px; height: 20px; border-radius: 50%;
    background: var(--ink); color: var(--card-taupe);
    font-size: 11px; display: inline-flex; align-items: center; justify-content: center;
    flex: none;
  }
  .brand-band {
    position: absolute; left: 0; right: 0; top: 116px; height: 70px;
    background: var(--band-dark);
    display: flex; align-items: center; padding-left: 40px;
  }
  .brand-name { font-size: 28px; white-space: nowrap; }
  .brand-name .bold {
    font-family: "Montserrat", "Century Gothic", sans-serif;
    font-weight: 700; color: var(--teal); text-transform: uppercase;
  }
  .brand-name .light {
    color: var(--white); text-transform: uppercase; letter-spacing: 1px;
  }
  .teal-edge {
    position: absolute; left: 0; top: 186px; bottom: 0; width: 10px;
    background: var(--teal);
  }
  .contact-main {
    position: absolute; left: 40px; top: 214px;
    font-size: 16px; line-height: 1.95;
  }
  .contact-main .row, .contact-side .row { display: flex; align-items: center; gap: 10px; }
  .contact-divider {
    position: absolute; left: 420px; top: 222px; width: 1px; height: 66px;
    background: var(--ink);
  }
  .contact-side {
    position: absolute; left: 440px; top: 214px;
    font-size: 16px; line-height: 1.95;
  }

  /* ---------- photo side ---------- */
  .card--photo { color: var(--white); }
  .interior-photo {
    position: absolute; inset: 0;
    background: linear-gradient(160deg, var(--photo-light) 0%, var(--photo-mid) 55%, var(--photo-dark) 100%);
  }
  .photo-band {
    position: absolute; left: 0; right: 0; top: 138px; height: 86px;
    background: rgba(42,41,41,.82);
    display: flex; align-items: center; padding-left: 40px;
  }
  .photo-band .brand-name { font-size: 28px; }
  .social-row {
    position: absolute; right: 60px; top: 236px;
    display: flex; gap: 12px;
  }
  .social-dot { width: 30px; height: 30px; border-radius: 50%; background: var(--teal); }
  .photo-url {
    position: absolute; right: 60px; top: 282px;
    font-size: 22px; letter-spacing: 1px;
  }
</style>
</head>
<body>

  <section class="card card--info">
    <div class="holder-name">Dominic Valtersen</div>
    <div class="holder-mobile"><span class="badge">M</span>917-526-0389</div>

    <div class="brand-band">
      <div class="brand-name"><span class="bold">Oak &amp; Meridian</span> <span class="light">Contracting</span></div>
    </div>
    <div class="teal-edge"></div>

    <div class="contact-main">
      <div class="row">318 fenwick st elm harbor, NY 10587</div>
      <div class="row"><span class="badge">E</span>harborkeybuild@mailbrook.com</div>
      <div class="row"><span class="badge">W</span>www.harborkeybuild.com</div>
    </div>
    <div class="contact-divider"></div>
    <div class="contact-side">
      <div class="row"><span class="badge">P</span>914 208 3916</div>
      <div class="row"><span class="badge">F</span>914 208 5523</div>
    </div>
  </section>

  <section class="card card--photo">
    <div class="interior-photo" role="img" aria-label="Photograph of a bright finished interior living space in muted grey tones"></div>
    <div class="photo-band">
      <div class="brand-name"><span class="bold">Oak &amp; Meridian</span> <span class="light">Contracting</span></div>
    </div>
    <div class="social-row">
      <span class="social-dot"></span>
      <span class="social-dot"></span>
      <span class="social-dot"></span>
      <span class="social-dot"></span>
    </div>
    <div class="photo-url">http://www.harborkeybuild.com</div>
  </section>

</body>
</html>
```